Seriöses Webdesign für innovatives Ingenieurbüro mit dem Schwerpunkt Eisenbahn Leit- und Sicherungstechnik
Zielgruppe
Die Webseite hat in erster Linie die Aufgabe zu informieren: An erster Stelle steht die Kontaktaufnahme und der Kompetenzbereich des Ingenieurbüros.
Folgende Kernkompetenzen sollen durch die Webseite transportiert werden:
Hardware-Entwicklung
Software-Entwicklung
Erneuerung alter Techniken
Begutachtung
Software für Lieferantenbewertung
Störungsmanagement(system)
Zielgruppe:
Die Webseite soll als Online-Visitenkarte für bestehende und neue Kontakte dienen. Gerade neue (Messe-)Kontakte erleben die Webseite als erste Anlaufstelle und erhalten einen Einblick in das vorhandene Leistungsspektrum des Ingenieurbüros und die Möglichkeiten der Kontaktaufnahme.

```html
<!DOCTYPE html>
<html lang="de">
<head>
<meta charset="utf-8">
<title>Veltrax – Ingenieurbüro für Verkehrstechnik</title>
<link href="https://fonts.googleapis.com/css2?family=Fira+Sans:wght@400;500;600&family=Source+Sans+3:wght@400;600;700&display=swap" rel="stylesheet">
<style>
:root{
  --sky:#7fc3e1;
  --sky-pale:#dcf0fb;
  --ink:#2d3a45;
  --ink-soft:#3a4853;
  --text:#2a2a2a;
  --accent:#4aa8d8;
  --white:#ffffff;
}
*{box-sizing:border-box;margin:0;padding:0}
html,body{width:1200px;height:2587px;overflow:hidden}
body{font-family:"Source Sans 3",sans-serif;color:var(--text);background:var(--white);position:relative}
.abs{position:absolute}
p{font-size:14.5px;line-height:20px}

.site-header{position:absolute;left:0;top:0;width:1200px;height:98px;background:var(--sky)}
.brand{position:absolute;left:178px;top:18px}
.brand-name{font-family:"Fira Sans",sans-serif;font-weight:600;font-size:40px;line-height:44px;color:var(--white)}
.brand-tag{font-size:14px;color:var(--ink);font-weight:600;margin-top:2px}
.lang{position:absolute;left:952px;top:38px;display:flex;gap:4px;font-size:11px;font-weight:700}
.lang span{padding:3px 8px;background:var(--white);color:var(--ink)}
.lang span.off{background:transparent}

.hero{position:absolute;left:0;top:98px;width:1200px;height:354px;
  background:
    radial-gradient(ellipse 360px 150px at 700px 170px,rgba(232,234,236,.85),rgba(232,234,236,0) 70%),
    linear-gradient(180deg,#7f8a99 0%,#9aa5b3 30%,#a7adb4 50%,#8d8478 70%,#6b5d50 88%,#4e463e 100%)}
.service-nav{position:absolute;left:178px;top:54px;width:282px;height:186px;background:var(--sky-pale);border-radius:6px;padding:14px 20px}
.service-nav a{display:block;font-size:14px;font-weight:600;color:var(--ink);text-decoration:none;height:27.4px;line-height:27px;padding-left:6px;border-bottom:1px solid var(--ink)}
.service-nav a:last-child{border-bottom:none}
.service-nav a.active{background:var(--ink);color:var(--white)}

.intro{position:absolute;left:0;top:452px;width:1200px;height:316px;background:var(--ink);color:var(--white)}
.intro h1{position:absolute;left:178px;top:38px;font-family:"Fira Sans",sans-serif;font-weight:400;font-size:42px;line-height:46px}
.intro-illustration{position:absolute;left:398px;top:28px;width:288px;height:96px;background:var(--ink-soft);border-radius:4px}
.intro h2{position:absolute;left:178px;top:136px;font-weight:400;font-size:20px;color:var(--sky)}
.intro p{position:absolute;left:178px;top:196px;width:400px;color:var(--white);line-height:22px}
.contact-btn{position:absolute;left:782px;top:114px;width:162px;height:40px;background:var(--sky);border-radius:3px;font-family:"Fira Sans",sans-serif;font-weight:500;font-size:22px;color:var(--ink);text-align:center;line-height:40px}
.contact-line{position:absolute;left:800px;font-size:14.5px;font-weight:700}
.contact-line.mail{color:var(--sky)}

.features{position:absolute;left:0;top:768px;width:1200px;height:357px}
.feature{position:absolute;top:52px;width:245px}
.feature h3{font-family:"Fira Sans",sans-serif;font-weight:500;font-size:22px;line-height:21px;color:var(--ink);position:absolute;left:62px;top:20px}
.feature svg{position:absolute;left:0;top:10px}
.feature .lead{position:absolute;top:78px;color:var(--accent);width:245px}
.feature .body{position:absolute;width:245px}

.rule{position:absolute;left:0;width:1200px;height:5px;background:var(--ink)}
.pattern-band{position:absolute;left:0;width:1200px;height:292px;background:linear-gradient(180deg,#d6d6d6,#e0e0e0)}
.col{position:absolute;width:245px}
.up{position:absolute;width:36px;height:36px}

.renewal{position:absolute;left:0;width:1200px}
.renewal h2{position:absolute;left:180px;top:48px;font-family:"Fira Sans",sans-serif;font-weight:500;font-size:32px;color:var(--ink)}
.relay{position:absolute;width:72px;height:176px;border-radius:4px}

.site-footer{position:absolute;left:0;top:2458px;width:1200px;height:129px;background:var(--sky)}
.site-footer .brand-name{position:absolute;left:178px;top:30px}
.footer-links{position:absolute;left:178px;top:96px;font-size:12.5px;font-weight:600;color:var(--ink)}
.footer-btn{position:absolute;top:48px;width:168px;height:32px;border:1px solid var(--white);border-radius:3px;color:var(--white);font-weight:700;font-size:14px;text-align:center;line-height:30px}
</style>
</head>
<body>

<header class="site-header">
  <div class="brand">
    <div class="brand-name">Veltrax</div>
    <div class="brand-tag">Ingenieurbüro für Verkehrstechnik</div>
  </div>
  <div class="lang"><span>DE</span><span class="off">ENG</span></div>
</header>

<section class="hero" role="img" aria-label="Foto: zwei Hochgeschwindigkeitszüge fahren aus einer Wartungshalle auf ein Gleis">
  <nav class="service-nav">
    <a>Software</a>
    <a>Hardware</a>
    <a class="active">Begutachtung</a>
    <a>Erneuerung alter Techniken</a>
    <a>Software für Lieferantenbewertung</a>
    <a>Störungsmanagement</a>
  </nav>
</section>

<section class="intro">
  <h1>Wir stellen<br>Weichen</h1>
  <div class="intro-illustration" role="img" aria-label="Illustration: gepunktete Linie von einem Bildschirm zu einem Gleisplan mit Weiche"></div>
  <h2>Maßgeschneiderte Softwarelösungen</h2>
  <p>Hier sollte ein Text stehen, der uns zum Vorteil gereift. Hier sollte ein Text stehen, der uns zum Vorteil gereift. Hier sollte ein Text stehen, der uns zum Vorteil</p>
  <div class="contact-btn">&gt;&gt; Kontakt</div>
  <div class="contact-line" style="top:170px">T 0 800 - 41 27 60 90</div>
  <div class="contact-line mail" style="top:196px">info@veltrax-ing.de</div>
</section>

<section class="features">
  <div class="feature" style="left:178px">
    <svg width="40" height="40" viewBox="0 0 40 40" fill="none" stroke="#2d3a45" stroke-width="2">
      <rect x="2" y="10" width="36" height="24" rx="2"/>
      <path d="M8 16h4M14 16h4M20 16h4M26 16h4M8 22h4M14 22h4M20 22h4M26 22h4M10 28h20"/>
      <path d="M20 10 C20 4 28 6 30 2"/>
    </svg>
    <h3>Hard-und Soft-<br>wareenwicklung</h3>
    <p class="lead">Hier sollte ein Text stehen, der uns zum Vorteil gereift. Hier sollte ein Text stehen.</p>
    <p class="body" style="top:158px">Hier sollte ein Text stehen, der uns zum Vorteil gereift. Hier sollte ein Text stehen. Hier sollte ein Text stehen, der uns zum Vorteil gereift. Hier sollte ein Text stehen.</p>
  </div>
  <div class="feature" style="left:496px">
    <svg width="36" height="54" viewBox="0 0 36 54" fill="#2d3a45">
      <rect x="14" y="0" width="8" height="4" rx="1"/>
      <rect x="2" y="6" width="32" height="38" rx="8"/>
      <rect x="7" y="12" width="22" height="12" rx="2" fill="#fff"/>
      <circle cx="10" cy="34" r="3" fill="#fff"/><circle cx="26" cy="34" r="3" fill="#fff"/>
      <path d="M6 44l-4 8h4l4-8zM30 44l4 8h-4l-4-8z"/>
    </svg>
    <h3 style="left:50px;top:22px">Spezialgebiete</h3>
    <p class="lead">Hier sollte ein Text stehen, der uns zum Vorteil gereift. Hier sollte ein Text stehen. Hier sollte ein Text stehen.Hier sollte ein Text stehen.</p>
    <p class="body" style="top:178px">Hier sollte ein Text stehen, der uns zum Vorteil gereift. Hier sollte ein</p>
  </div>
  <div class="feature" style="left:781px">
    <svg width="36" height="36" viewBox="0 0 36 36" fill="none" stroke="#2d3a45" stroke-width="5">
      <line x1="4" y1="4" x2="32" y2="32"/><line x1="32" y1="4" x2="4" y2="32"/>
    </svg>
    <h3 style="left:52px">Kundenspezifische<br>Lösungen</h3>
    <p class="lead">Hier sollte ein Text stehen, der uns zum Vorteil gereift. Hier sollte ein Text stehen.</p>
    <p class="body" style="top:158px">Hier sollte ein Text stehen, der uns zum Vorteil gereift. Hier sollte ein Text stehen. Hier sollte ein Text stehen, der uns zum Vorteil gereift. Hier sollte ein Text stehen.</p>
  </div>
</section>

<div class="rule" style="top:1127px"></div>
<section class="pattern-band" style="top:1134px" role="img" aria-label="Hintergrund: geprägter Gleisplan eines Stellwerks in Hellgrau">
  <p class="col" style="left:178px;top:54px">Hier sollte ein Text stehen, der uns zum Vorteil gereift. Hier sollte ein Text stehen.</p>
  <p class="col" style="left:178px;top:134px">Hier sollte ein Text stehen, der uns zum Vorteil gereift. Hier sollte ein Text stehen. Hier sollte ein Text stehen, der uns zum Vorteil gereift. Hier sollte ein Text stehen.</p>
  <p class="col" style="left:474px;top:54px">Hier sollte ein Text stehen, der uns zum Vorteil gereift. Hier sollte ein Text stehen.</p>
  <p class="col" style="left:474px;top:134px">Hier sollte ein Text stehen, der uns zum Vorteil gereift. Hier sollte ein Text stehen. Hier sollte ein Text stehen, der uns zum Vorteil gereift. Hier sollte ein Text stehen.</p>
  <p class="col" style="left:777px;top:54px">Hier sollte ein Text stehen, der uns zum Vorteil gereift. Hier sollte ein Text stehen.</p>
  <p class="col" style="left:777px;top:134px">Hier sollte ein Text stehen, der uns zum Vorteil gereift. Hier sollte ein Text stehen. Hier sollte ein Text stehen, der uns zum Vorteil gereift. Hier sollte ein Text stehen.</p>
  <svg class="up" style="left:1002px;top:236px" viewBox="0 0 36 36"><circle cx="18" cy="18" r="18" fill="#2d3a45"/><path d="M10 21l8-8 8 8" fill="none" stroke="#fff" stroke-width="2.5"/></svg>
</section>
<div class="rule" style="top:1432px"></div>

<section class="renewal" style="top:1437px;height:350px">
  <h2>Erneuerung der alten Technik</h2>
  <p class="col" style="left:178px;top:120px">Hier sollte ein Text stehen, der uns zum Vorteil gereift. Hier sollte ein Text stehen.</p>
  <p class="col" style="left:178px;top:200px">Hier sollte ein Text stehen, der uns zum Vorteil gereift. Hier sollte ein Text stehen. Hier sollte ein Text stehen, der uns zum Vorteil gereift. Hier sollte ein Text stehen.</p>
  <p class="col" style="left:474px;top:120px">Hier sollte ein Text stehen, der uns zum Vorteil gereift. Hier sollte ein Text stehen.</p>
  <p class="col" style="left:474px;top:200px">Hier sollte ein Text stehen, der uns zum Vorteil gereift. Hier sollte ein Text stehen. Hier sollte ein Text stehen, der uns zum Vorteil gereift. Hier sollte ein Text stehen.</p>
  <div class="relay" style="left:782px;top:96px;background:linear-gradient(180deg,#9aa0a4,#c98a3c 40%,#b9bcbf)" role="img" aria-label="Foto: altes Relais mit Spule im Glasgehäuse"></div>
  <div class="relay" style="left:902px;top:96px;background:linear-gradient(180deg,#5a5f63,#3f7d4a 45%,#b7bbbe)" role="img" aria-label="Foto: Relais mit grüner Platine im Glasgehäuse"></div>
  <svg class="up" style="left:1002px;top:289px" viewBox="0 0 36 36"><circle cx="18" cy="18" r="18" fill="#2d3a45"/><path d="M10 21l8-8 8 8" fill="none" stroke="#fff" stroke-width="2.5"/></svg>
</section>

<div class="rule" style="top:1792px"></div>
<section class="pattern-band" style="top:1799px" role="img" aria-label="Hintergrund: geprägter Gleisplan eines Stellwerks in Hellgrau">
  <p class="col" style="left:178px;top:54px">Hier sollte ein Text stehen, der uns zum Vorteil gereift. Hier sollte ein Text stehen.</p>
  <p class="col" style="left:178px;top:134px">Hier sollte ein Text stehen, der uns zum Vorteil gereift. Hier sollte ein Text stehen. Hier sollte ein Text stehen, der uns zum Vorteil gereift. Hier sollte ein Text stehen.</p>
  <p class="col" style="left:474px;top:54px">Hier sollte ein Text stehen, der uns zum Vorteil gereift. Hier sollte ein Text stehen.</p>
  <p class="col" style="left:474px;top:134px">Hier sollte ein Text stehen, der uns zum Vorteil gereift. Hier sollte ein Text stehen. Hier sollte ein Text stehen, der uns zum Vorteil gereift. Hier sollte ein Text stehen.</p>
  <p class="col" style="left:777px;top:54px">Hier sollte ein Text stehen, der uns zum Vorteil gereift. Hier sollte ein Text stehen.</p>
  <p class="col" style="left:777px;top:134px">Hier sollte ein Text stehen, der uns zum Vorteil gereift. Hier sollte ein Text stehen. Hier sollte ein Text stehen, der uns zum Vorteil gereift. Hier sollte ein Text stehen.</p>
  <svg class="up" style="left:1002px;top:238px" viewBox="0 0 36 36"><circle cx="18" cy="18" r="18" fill="#2d3a45"/><path d="M10 21l8-8 8 8" fill="none" stroke="#fff" stroke-width="2.5"/></svg>
</section>
<div class="rule" style="top:2097px"></div>

<section class="renewal" style="top:2102px;height:356px">
  <h2>Erneuerung der alten Technik</h2>
  <p class="col" style="left:178px;top:120px">Hier sollte ein Text stehen, der uns zum Vorteil gereift. Hier sollte ein Text stehen.</p>
  <p class="col" style="left:178px;top:200px">Hier sollte ein Text stehen, der uns zum Vorteil gereift. Hier sollte ein Text stehen. Hier sollte ein Text stehen, der uns zum Vorteil gereift. Hier sollte ein Text stehen.</p>
  <p class="col" style="left:474px;top:120px">Hier sollte ein Text stehen, der uns zum Vorteil gereift. Hier sollte ein Text stehen.</p>
  <p class="col" style="left:474px;top:200px">Hier sollte ein Text stehen, der uns zum Vorteil gereift. Hier sollte ein Text stehen. Hier sollte ein Text stehen, der uns zum Vorteil gereift. Hier sollte ein Text stehen.</p>
  <div class="relay" style="left:782px;top:96px;background:linear-gradient(180deg,#9aa0a4,#c98a3c 40%,#b9bcbf)" role="img" aria-label="Foto: altes Relais mit Spule im Glasgehäuse"></div>
  <div class="relay" style="left:902px;top:96px;background:linear-gradient(180deg,#5a5f63,#3f7d4a 45%,#b7bbbe)" role="img" aria-label="Foto: Relais mit grüner Platine im Glasgehäuse"></div>
  <svg class="up" style="left:1002px;top:288px" viewBox="0 0 36 36"><circle cx="18" cy="18" r="18" fill="#2d3a45"/><path d="M10 21l8-8 8 8" fill="none" stroke="#fff" stroke-width="2.5"/></svg>
</section>

<footer class="site-footer">
  <div class="brand-name">Veltrax</div>
  <div class="footer-links">Startseite &nbsp;•&nbsp; AGB &nbsp;•&nbsp; Bankverbindung &nbsp;•&nbsp; Datenschutz &nbsp;•&nbsp; Impressum</div>
  <div class="footer-btn" style="left:685px">Nachricht senden &gt;&gt;</div>
  <div class="footer-btn" style="left:872px">Downloads &gt;&gt;</div>
</footer>

</body>
</html>
```